Olvar business stationery
Purified water company
Simple
Rodrigo Lemus
Gerente General
Calle 38 con Avenida Tzabalché
entre 164 y 166
Colonia Vista de Orquídeas
Mérida, Yucatán
rlem@purificadoraolvar-mx.com
www.purificadoraolvar-mx.com
- The logo font is Quadranta
- We would like all stationary, including letterhead, envelopes, business card, presentation folder, compliment card and fax cover
- Color gradient of blue
Light blue C=50 M=1 Y=0 K=0
Blue C=92 M=63 Y=1 K=0
Stroke light blue C=27 M=0 Y=1 K=0
siempre contigo...
- Name and image should be integrated in the design of the stationary
- Designers can split the name (quadranta font) and the waterfall image to use as they like during their designs

```html
<!DOCTYPE html>
<html lang="es">
<head>
<meta charset="utf-8">
<title>Olvar — Tarjeta de presentación</title>
<link rel="stylesheet" href="https://fonts.googleapis.com/css2?family=PT+Sans:wght@400;700&display=swap">
<style>
  :root {
    --blue-deep: #1769b4;
    --blue-mid: #3f97d6;
    --blue-light: #86ccf2;
    --stroke-light: #bde5f7;
    --green: #8bb61c;
    --green-dark: #6f9a12;
    --white: #ffffff;
    --page: #f2f2f2;
  }
  * { margin: 0; padding: 0; box-sizing: border-box; }
  html, body {
    width: 1200px; height: 778px; overflow: hidden;
    background: var(--page);
    font-family: "PT Sans", Arial, sans-serif;
  }
  .business-card {
    position: relative;
    width: 1200px; height: 778px;
    background: var(--white);
    overflow: hidden;
  }
  .card-waves { position: absolute; inset: 0; width: 1200px; height: 778px; }
  .holder {
    position: absolute; top: 100px; right: 70px;
    text-align: right;
  }
  .holder-name {
    font-size: 42px; font-weight: 700; color: var(--blue-deep);
    line-height: 1.1;
  }
  .holder-role {
    font-size: 34px; font-weight: 700; color: var(--green-dark);
    line-height: 1.2;
  }
  .brand {
    position: absolute; left: 95px; top: 250px;
    display: flex; align-items: center; gap: 22px;
  }
  .brand-dot {
    width: 46px; height: 46px; border-radius: 50%;
    background: var(--blue-light);
  }
  .brand-name {
    font-size: 150px; font-weight: 400; color: var(--blue-mid);
    line-height: 1; letter-spacing: 2px;
  }
  .address {
    position: absolute; right: 70px; top: 400px;
    text-align: right; color: var(--white);
    font-size: 26px; line-height: 1.36;
    font-style: normal;
  }
  .contact {
    position: absolute; right: 70px; top: 572px;
    list-style: none; color: var(--white);
    font-size: 26px; line-height: 1.4;
    text-align: right;
  }
  .contact li { display: flex; justify-content: flex-end; align-items: center; gap: 12px; }
  .contact svg { width: 20px; height: 20px; flex: none; }
</style>
</head>
<body>
<main class="business-card">
  <svg class="card-waves" viewBox="0 0 1200 778" aria-hidden="true">
    <defs>
      <linearGradient id="water" x1="0" y1="0" x2="0.3" y2="1">
        <stop offset="0" stop-color="var(--blue-light)"/>
        <stop offset="0.45" stop-color="var(--blue-mid)"/>
        <stop offset="1" stop-color="var(--blue-deep)"/>
      </linearGradient>
    </defs>
    <path class="wave-green" d="M0 470 C 230 560 480 530 700 360 S 1040 200 1200 175 L1200 778 L0 778 Z" fill="var(--green)"/>
    <path class="wave-stroke" d="M0 508 C 230 598 480 568 700 398 S 1040 238 1200 213 L1200 778 L0 778 Z" fill="var(--stroke-light)"/>
    <path class="wave-water" d="M0 518 C 230 608 480 578 700 408 S 1040 248 1200 223 L1200 778 L0 778 Z" fill="url(#water)"/>
  </svg>

  <header class="holder">
    <h1 class="holder-name">Rodrigo Lemus</h1>
    <p class="holder-role">Gerente General</p>
  </header>

  <div class="brand">
    <span class="brand-dot"></span>
    <span class="brand-name">Olvar</span>
  </div>

  <address class="address">
    Calle 38 con Avenida Tzabalché<br>
    entre 164 y 166<br>
    Colonia Vista de Orquídeas<br>
    Mérida, Yucatán
  </address>

  <ul class="contact">
    <li>999-4812075
      <svg viewBox="0 0 20 20" aria-label="teléfono"><rect x="6" y="2" width="8" height="16" rx="2" fill="none" stroke="#fff" stroke-width="2"/><circle cx="10" cy="14.5" r="1.2" fill="#fff"/></svg>
    </li>
    <li>rlem@purificadoraolvar-mx.com
      <svg viewBox="0 0 20 20" aria-label="correo"><rect x="2" y="4" width="16" height="12" fill="#fff"/><path d="M2 4 L10 11 L18 4" fill="none" stroke="var(--blue-mid)" stroke-width="1.5"/></svg>
    </li>
    <li>www.purificadoraolvar-mx.com
      <svg viewBox="0 0 20 20" aria-label="sitio web"><circle cx="10" cy="10" r="7.5" fill="#fff"/><path d="M2.5 10 H17.5 M10 2.5 C6 6 6 14 10 17.5 M10 2.5 C14 6 14 14 10 17.5" fill="none" stroke="var(--blue-mid)" stroke-width="1.2"/></svg>
    </li>
  </ul>
</main>
</body>
</html>
```